Harbourline Strategy Group firm

I need a business card that is succint for a Brisbane based business called Harbourline Strategy Group Pty Ltd.
We bridge the gaps between People, Process and Technology.

We are a specialist operational excellence firm, delivering strategic consulting and business advisory services in six core capabilities, across all industries and all business lines to improve performance, efficiency, profitability, automation and scalability, for clients across Australia &New Zealand.
Updates

Hi Designers, I have uploaded the logo in 3D .png format, to assist in card design.

Target Market(s)

Project Management professionals, IT professionals, corporate and government clients managing transitioning or transformation projects.

Contact Information for Business Card

Harbourline Strategy Group Pty Ltd

Daniel Ferreira
Principal Consultant

mobile: +61 417 260 315
email: daniel@harbourlinestrategygroup.com.au
webpage: www.harbourlinestrategygroup.com

professional services: strategic advisors,

Font styles to use
Sans Serif

Requirements
Must have
• Business name: Harbourline Strategy Group
logo: attached
Contact person: Daniel Ferreira
Title: Principal Consultant
contact details:
mobile +61 417 260
email: daniel@HarbourlineStrategyGroup.com.au
website: HarbourlineStrategyGroup.com

on back side with logo include: A.B.N. 58210947362

professional services offered: Business Analysis, Strategic Advisory
Nice to have
• QR code
Should not have
• contacts picture

```html
<!DOCTYPE html>
<html lang="en">
<head>
<meta charset="utf-8">
<title>Harbourline Strategy Group — Business Card</title>
<link rel="stylesheet" href="https://fonts.googleapis.com/css2?family=Oswald:wght@300;400;500&display=swap">
<style>
  :root {
    --page: #ececec;
    --navy: #1f2442;
    --navy-tone: #252b4d;
    --red: #d7232d;
    --white: #f4f4f6;
    --muted: #9aa0bd;
  }
  * { margin: 0; padding: 0; box-sizing: border-box; }
  html, body {
    width: 1200px;
    height: 900px;
    overflow: hidden;
    background: var(--page);
    font-family: "Oswald", "Arial Narrow", sans-serif;
  }
  .canvas {
    position: relative;
    width: 1200px;
    height: 900px;
  }
  .card {
    position: absolute;
    left: 280px;
    width: 640px;
    height: 366px;
    background: var(--navy);
    box-shadow: 0 10px 28px rgba(0, 0, 0, 0.18);
    overflow: hidden;
  }
  .card--front { top: 64px; }
  .card--back { top: 470px; }

  /* Front */
  .brand {
    position: absolute;
    left: 40px;
    top: 38px;
    display: flex;
    align-items: center;
    gap: 10px;
  }
  .brand__square {
    width: 14px;
    height: 14px;
    background: var(--red);
    flex: none;
  }
  .brand__name {
    color: var(--white);
    font-weight: 500;
    font-size: 22px;
    letter-spacing: 0.04em;
    text-transform: uppercase;
    white-space: nowrap;
  }
  .person {
    position: absolute;
    left: 40px;
    top: 150px;
    text-transform: uppercase;
  }
  .person__name {
    color: var(--red);
    font-weight: 400;
    font-size: 26px;
    letter-spacing: 0.02em;
    line-height: 1.1;
  }
  .person__title {
    color: var(--white);
    font-weight: 300;
    font-size: 17px;
    letter-spacing: 0.03em;
    margin-top: 4px;
  }
  .contact {
    position: absolute;
    left: 40px;
    bottom: 34px;
    list-style: none;
    font-weight: 300;
    font-size: 13.5px;
    line-height: 1.55;
    color: var(--white);
    text-transform: uppercase;
    letter-spacing: 0.02em;
  }
  .contact__web { color: var(--red); }

  /* Back */
  .back-pattern {
    position: absolute;
    inset: 0;
    background: linear-gradient(135deg, var(--navy) 0%, var(--navy-tone) 50%, var(--navy) 100%);
  }
  .back-brand {
    position: absolute;
    right: 56px;
    top: 70px;
    display: flex;
    align-items: center;
    gap: 8px;
  }
  .back-brand .brand__name { font-size: 15px; }
  .back-brand .brand__square { width: 10px; height: 10px; }
  .back-info {
    position: absolute;
    left: 0;
    right: 0;
    bottom: 34px;
    text-align: center;
    text-transform: uppercase;
  }
  .tagline {
    color: var(--red);
    font-weight: 400;
    font-size: 14px;
    letter-spacing: 0.42em;
    margin-right: -0.42em;
  }
  .services {
    margin-top: 14px;
    color: var(--white);
    font-weight: 300;
    font-size: 12px;
    letter-spacing: 0.16em;
  }
  .abn {
    margin-top: 8px;
    color: var(--muted);
    font-weight: 300;
    font-size: 11px;
    letter-spacing: 0.12em;
  }
</style>
</head>
<body>
<main class="canvas">
  <section class="card card--front" aria-label="Business card front">
    <div class="brand">
      <span class="brand__square"></span>
      <span class="brand__name">Harbourline Strategy Group</span>
    </div>
    <div class="person">
      <h1 class="person__name">Daniel Ferreira</h1>
      <p class="person__title">Principal Consultant</p>
    </div>
    <ul class="contact">
      <li class="contact__phone">+61 417 260 315</li>
      <li class="contact__email">daniel@harbourlinestrategygroup.com.au</li>
      <li class="contact__web">www.harbourlinestrategygroup.com</li>
    </ul>
  </section>

  <section class="card card--back" aria-label="Business card back">
    <div class="back-pattern" role="img" aria-label="Faint tone-on-tone repeating brand pattern"></div>
    <div class="back-brand">
      <span class="brand__square"></span>
      <span class="brand__name">Harbourline Strategy Group</span>
    </div>
    <div class="back-info">
      <p class="tagline">Strategic Advisors</p>
      <p class="services">Business Analysis &nbsp;·&nbsp; Strategic Advisory</p>
      <p class="abn">A.B.N. 58210947362</p>
    </div>
  </section>
</main>
</body>
</html>
```